Neighbourhood assistance

I need an app design for a social idea. Each person has some skils and could offer some assistance to some of his neighbours. With this app I will bring people together. For free or also for some money.That doesn't matter.

Please have a look into my pptx file which should give you an idea about the upcoming app.

Industry/Entity Type

Social

```html
<!DOCTYPE html>
<html lang="de">
<head>
<meta charset="utf-8">
<title>Angebote für Hütedienst</title>
<link rel="stylesheet" href="https://fonts.googleapis.com/css2?family=Dosis:wght@400;500&family=Raleway:wght@400&display=swap">
<style>
  :root {
    --purple: #990fbf;
    --purple-dark: #79069a;
    --white: #ffffff;
    --green: #0bd38a;
    --map-base: #e6e2d6;
    --map-road: #f3e78a;
    --pin: #e8321c;
  }
  * { margin: 0; padding: 0; box-sizing: border-box; }
  html, body { width: 676px; height: 1200px; overflow: hidden; }
  body {
    position: relative;
    background: var(--purple);
    font-family: "Raleway", sans-serif;
    color: var(--white);
  }
  .status-bar {
    position: absolute; left: 0; top: 0; width: 676px; height: 42px;
    display: flex; align-items: center; justify-content: space-between;
    padding: 0 16px; font-family: "Helvetica Neue", Arial, sans-serif;
    font-size: 23px; font-weight: 600;
  }
  .status-left, .status-right { display: flex; align-items: center; gap: 8px; }
  .status-time { position: absolute; left: 0; right: 0; text-align: center; pointer-events: none; }
  .nav-bar {
    position: absolute; left: 0; top: 42px; width: 676px; height: 90px;
    background: var(--purple-dark);
  }
  .back-button {
    position: absolute; left: 18px; top: 30px; width: 77px; height: 38px;
    background: var(--white); color: var(--purple-dark); border-radius: 2px;
    font-size: 18px; display: flex; align-items: center; justify-content: center;
  }
  .screen-title {
    position: absolute; left: 121px; top: 22px;
    font-family: "Dosis", sans-serif; font-weight: 400; font-size: 39px;
    letter-spacing: 0.5px; line-height: 1.2;
  }
  .view-toggle {
    position: absolute; left: 99px; top: 214px; width: 493px; height: 45px;
    display: flex; border: 1.5px solid var(--white); border-radius: 3px; overflow: hidden;
  }
  .view-toggle span {
    flex: 1; display: flex; align-items: center; justify-content: center;
    font-size: 29px; line-height: 1;
  }
  .view-toggle .is-active { background: var(--white); color: var(--purple-dark); }
  .offer-map {
    position: absolute; left: 92px; top: 311px; width: 528px; height: 316px;
    background: linear-gradient(135deg, var(--map-base) 0%, #ece8dc 45%, #dcd9cc 100%);
  }
  .offer-map svg { position: absolute; left: 0; top: 0; }
  .select-button {
    position: absolute; left: 113px; top: 715px; width: 482px; height: 85px;
    background: var(--green); border-radius: 3px;
    display: flex; align-items: center; justify-content: center;
    font-size: 30px;
  }
</style>
</head>
<body>
  <header class="status-bar">
    <div class="status-left">
      <svg width="84" height="14" viewBox="0 0 84 14" aria-hidden="true">
        <g fill="#fff"><circle cx="7" cy="7" r="6"/><circle cx="23" cy="7" r="6"/><circle cx="39" cy="7" r="6"/><circle cx="55" cy="7" r="6"/></g>
        <circle cx="71" cy="7" r="5.2" fill="none" stroke="#fff" stroke-width="1.5"/>
      </svg>
      <span>Nexa</span>
      <svg width="24" height="18" viewBox="0 0 24 18" aria-hidden="true" fill="none" stroke="#fff" stroke-width="2.6" stroke-linecap="round">
        <path d="M2 6 Q12 -2 22 6"/><path d="M6 10 Q12 5 18 10"/><circle cx="12" cy="15" r="1.8" fill="#fff" stroke="none"/>
      </svg>
    </div>
    <div class="status-time">4:20 PM</div>
    <div class="status-right">
      <svg width="24" height="24" viewBox="0 0 24 24" aria-hidden="true" fill="none" stroke="#fff" stroke-width="2">
        <path d="M20 12a8 8 0 1 1-3-6.2"/><path d="M17 2v4h-4"/><rect x="9" y="11" width="6" height="5" fill="#fff" stroke="none"/><path d="M10 11V9.5a2 2 0 0 1 4 0V11"/>
      </svg>
      <span>100%</span>
      <svg width="46" height="22" viewBox="0 0 46 22" aria-hidden="true">
        <rect x="1" y="1" width="40" height="20" rx="3" fill="none" stroke="#fff" stroke-width="1.6"/>
        <rect x="3.5" y="3.5" width="35" height="15" rx="1.5" fill="#fff"/>
        <rect x="42" y="7" width="3" height="8" rx="1" fill="#fff"/>
      </svg>
    </div>
  </header>

  <nav class="nav-bar">
    <div class="back-button">Back</div>
    <h1 class="screen-title">ANGEBOTE FÜR HÜTEDIENST</h1>
  </nav>

  <div class="view-toggle">
    <span>Liste</span>
    <span class="is-active">Karte</span>
  </div>

  <div class="offer-map" role="img" aria-label="Stadtplan mit den Standorten der Angebote in der Nachbarschaft">
    <svg width="528" height="316" viewBox="0 0 528 316" aria-hidden="true">
      <g fill="var(--pin)">
        <path d="M263 114c-7-10-13-18-13-26a13 13 0 0 1 26 0c0 8-6 16-13 26z"/>
        <path d="M157 187c-7-10-13-18-13-26a13 13 0 0 1 26 0c0 8-6 16-13 26z"/>
        <path d="M292 244c-7-10-13-18-13-26a13 13 0 0 1 26 0c0 8-6 16-13 26z"/>
        <path d="M471 205c-7-10-13-18-13-26a13 13 0 0 1 26 0c0 8-6 16-13 26z"/>
      </g>
      <g fill="#fff" opacity="0.55">
        <circle cx="263" cy="88" r="4.5"/><circle cx="157" cy="161" r="4.5"/>
        <circle cx="292" cy="218" r="4.5"/><circle cx="471" cy="179" r="4.5"/>
      </g>
    </svg>
  </div>

  <div class="select-button">Bitte auswählen</div>
</body>
</html>
```